Give Tall Oak Ridge an Online Presence!

Tall Oak Ridge Property Maintenance is an Australian Owned property maintenance company who needs a stand out online presence.

TOR maintains many buildings and sites and wants to appeal to a corporate professional market with their brand new website. TOR is essentially a handyman service offering all maintenance services to home owners, office managers, real estate agents and strata managers.

The Website:
We need a corporate website that appeals to our broader customer base (property owners, property managers, office managers) the copy is being written by a professional so use filler text for now.

Things that we want:
Home page that sets us apart and appeals to the corporate and residential market. The home page needs to not focus on either the residential or commercial market. The home page should focus on our logo and branding. We have a logo already and it is attached to the brief, please use it and try to consider the colour pallette that goes with it. Whilst we want the site to appear strong and manly it is important to remember that 95% of our customers are female so we need the site to be appealing to women. Women need to believe that we are strong, dependable and trustworthy.
We'd like a quote page and potentially also the ability to get a quote from the home page (please don't put it in if it ruins the overall feel of the home page)
An "about us" page
A contact us page
A blog that's built in (we don't want to link to an external blog)
(overall we'd expect to have 6 or 7 pages total)

The site will also need coding - we expect this to be done in a separate project but need you to consider a few things about the coding side of things.

It needs to be iPhone and iPad compatible.

We'd like you to suggest the best CMS that you would use or if you would suggest not using a CMS please let us know with your submissions.

Target Market(s)

Property owners, office managers and property managers who need maintenance on buildings (So all of them)

Industry/Entity Type

Property Maintenance

Requirements
Must have
• Our Logo
Home page
About Us
Residential
Commercial
Real Estate/Strata
Contact Us/Quote
Blog
Nice to have
• Quote form included in home page
Movement on the home page at least
Should not have
• other logos, too much colour
NO FLASH

```html
<!DOCTYPE html>
<html lang="en">
<head>
<meta charset="utf-8">
<title>Tall Oak Ridge Property Maintenance</title>
<link href="https://fonts.googleapis.com/css2?family=Oswald:wght@400;500&family=Montserrat:wght@700;800&family=Open+Sans:wght@400;600;700&display=swap" rel="stylesheet">
<style>
:root{
  --orange:#f7901e;
  --orange-dark:#e07c0c;
  --ink:#1f1f1f;
  --charcoal:#2b2b2b;
  --page:#ffffff;
  --canvas:#e8e8e8;
  --muted:#8a8a8a;
  --light:#f3f3f3;
  --blue:#1e88c8;
  --heading-blue:#1a7fc1;
}
*{box-sizing:border-box;margin:0;padding:0}
html,body{width:939px;height:1200px;overflow:hidden}
body{background:var(--canvas);font-family:"Open Sans",Arial,sans-serif;color:#555;position:relative}
.abs{position:absolute}
.top-band{left:0;top:0;width:939px;height:105px;background:linear-gradient(#e2e2e2,#ececec)}
.brand-name{left:134px;top:30px;width:128px;font-family:"Oswald",sans-serif;font-weight:500;font-size:22px;line-height:24px;color:var(--ink);text-align:center}
.social{left:684px;top:13px;display:flex;gap:8px}
.social span{width:21px;height:21px;border-radius:3px;background:#9a9a9a}
.top-links{left:670px;top:50px;font-size:9px;color:#666}
.call{left:584px;top:63px;display:flex;align-items:center;gap:8px}
.call small{font-size:9px;color:#888}
.call svg{width:14px;height:16px}
.call strong{font-family:"Montserrat",sans-serif;font-size:22px;color:var(--ink)}
.nav-band{left:0;top:105px;width:939px;height:34px;background:var(--orange)}
.logo-box{left:128px;top:100px;width:132px;height:40px;background:var(--orange-dark);color:#fff;font-family:"Oswald",sans-serif;font-size:12px;line-height:13px;text-align:center;padding-top:7px}
.nav{left:266px;top:105px;height:34px;display:flex;align-items:center;font-family:"Oswald",sans-serif;font-size:12.5px;color:#fff;text-transform:uppercase;white-space:nowrap}
.nav a{color:#fff;text-decoration:none}
.nav a.active{color:var(--ink);border-bottom:2px solid var(--ink)}
.nav i{font-style:normal;margin:0 8px;font-size:7px}
.search{left:691px;top:113px;width:112px;height:19px;background:#fff;border-radius:2px;font-size:9px;color:#aaa;padding:4px 7px}
.hero-bg{left:0;top:139px;width:939px;height:310px;background:linear-gradient(90deg,#9a9a9a,#c8c8c8 40%,#b5b5b5 70%,#8c8c8c)}
.hero{left:134px;top:139px;width:671px;height:310px;background:linear-gradient(#2d2d2d,#3c3c3c 60%,#2a2a2a)}
.hero-kicker{left:168px;top:200px;font-family:"Montserrat",sans-serif;font-size:14px;color:#fff}
.hero-title{left:166px;top:213px;font-family:"Montserrat",sans-serif;font-weight:800;font-size:40px;color:#fff;letter-spacing:-1px}
.hero-sub{left:168px;top:256px;font-family:"Montserrat",sans-serif;font-size:14px;color:#fff}
.hero-list{left:168px;top:288px;list-style:none;font-size:11.5px;color:#e6e6e6;line-height:17.5px}
.hero-list li{display:flex;align-items:center;gap:8px}
.hero-list svg{width:9px;height:9px}
.btn-orange{left:168px;top:372px;width:98px;height:25px;background:var(--orange);color:#fff;font-size:10px;font-weight:600;text-align:center;line-height:25px}
.hero-photo{left:450px;top:145px;width:355px;height:304px;background:radial-gradient(ellipse at 60% 55%,#5a5a5a,#333 70%)}
.page{left:134px;top:449px;width:671px;height:581px;background:var(--page)}
.feat-title{left:146px;top:458px;display:flex;align-items:center;gap:6px;font-family:"Montserrat",sans-serif;font-size:21px;color:var(--ink)}
.feat-title svg{width:20px;height:20px}
.rule{left:146px;top:488px;width:647px;height:1px;background:#e2e2e2}
.card{top:509px;width:154px;height:179px;background:var(--light);border:1px solid #e2e2e2}
.card .ph{height:79px}
.card h3{font-family:"Oswald",sans-serif;font-weight:400;font-size:12px;color:var(--heading-blue);margin:7px 0 3px 9px}
.card p{font-size:7.6px;line-height:9.6px;color:#999;margin:0 9px}
.card .arrow{position:absolute;right:0;bottom:0;width:21px;height:21px;background:var(--blue)}
.col{top:715px;width:197px;height:190px}
.col h4{font-family:"Oswald",sans-serif;font-weight:400;font-size:13px;color:var(--ink);margin-bottom:7px}
.col .ph{height:75px}
.col p{font-size:8.5px;line-height:12px;color:#555;margin-top:7px}
.btn{height:17px;font-size:8px;font-weight:700;color:#fff;display:flex;align-items:center;justify-content:center;gap:4px}
.testi h4{color:var(--orange)}
.quote-box{position:absolute;left:0;top:26px;width:197px;height:108px;background:var(--light);padding:10px 12px;font-size:8px;line-height:11px;color:#666}
.quote-box::after{content:"";position:absolute;left:20px;bottom:-8px;border:8px solid transparent;border-top-color:var(--light);border-bottom:0}
.author{position:absolute;left:47px;top:140px;font-size:9.5px;font-weight:700;color:var(--orange)}
.role{position:absolute;left:47px;top:153px;font-size:7.5px;color:#777}
.view-all{position:absolute;left:146px;top:167px;width:61px;background:var(--charcoal)}
.partners-label{left:134px;top:932px;width:671px;font-size:7px;color:#999;letter-spacing:.5px;padding-left:30px;border-top:1px solid #e6e6e6;padding-top:2px}
.partner{top:950px;width:98px;text-align:center}
.partner span{display:block;width:54px;height:30px;margin:0 auto 6px;background:#cfcfcf;border-radius:3px}
.partner small{font-size:7px;color:#888}
.footer{left:134px;top:1030px;width:671px;height:67px;background:var(--charcoal)}
.footer h5{position:absolute;left:15px;top:15px;font-family:"Montserrat",sans-serif;font-size:11px;color:#fff}
.footer nav{position:absolute;left:15px;top:34px;width:460px;font-size:8px;color:#999;line-height:16px}
.footer nav i{font-style:normal;margin:0 6px}
.foot-badge{position:absolute;right:16px;top:15px;width:110px;height:30px;background:var(--orange);color:#fff;font-family:"Oswald",sans-serif;font-size:9px;line-height:11px;text-align:center;padding-top:4px}
.bottom{left:0;top:1106px;width:939px;text-align:center}
.bottom .label{font-size:9px;color:#555}
.bottom .phone{display:inline-block;margin-top:4px;width:143px;height:20px;background:#555;color:#fff;font-size:13px;line-height:20px;border-radius:2px}
.bottom .fine{font-size:7.5px;color:#888;line-height:10px;margin-top:3px}
</style>
</head>
<body>
<div class="abs top-band"></div>
<div class="abs brand-name">TALL OAK RIDGE</div>
<div class="abs social"><span></span><span></span><span></span><span></span><span></span></div>
<div class="abs top-links">Real Estate/Strata &nbsp;|&nbsp; Quote</div>
<div class="abs call"><small>Call Us</small>
  <svg viewBox="0 0 14 16" aria-hidden="true"><rect x="1" y="1" width="12" height="14" rx="2" fill="#777"/><rect x="3" y="3" width="8" height="4" fill="#ddd"/></svg>
  <strong>0400 555 017</strong></div>

<div class="abs nav-band"></div>
<div class="abs logo-box">TALL OAK RIDGE<br>PROPERTY MAINTENANCE</div>
<nav class="abs nav">
  <a class="active">Home</a><i>●</i><a>About Us</a><i>●</i><a>Residential</a><i>●</i><a>Commercial</a><i>●</i><a>Blog</a><i>●</i><a>Contact Us</a>
</nav>
<div class="abs search">Search</div>

<div class="abs hero-bg" role="img" aria-label="Street of suburban houses in greyscale"></div>
<div class="abs hero"></div>
<div class="abs hero-photo" role="img" aria-label="Two handymen in black uniforms with tools and a level"></div>
<div class="abs hero-kicker">JUST SOME OF WHAT THE</div>
<div class="abs hero-title">TALL OAK RIDGE</div>
<div class="abs hero-sub">CAN DO FOR YOU</div>
<ul class="abs hero-list">
  <li><svg viewBox="0 0 10 10"><path d="M1 5l3 3 5-7" stroke="#f7901e" stroke-width="2" fill="none"/></svg>All commercial and residential handyman work</li>
  <li><svg viewBox="0 0 10 10"><path d="M1 5l3 3 5-7" stroke="#f7901e" stroke-width="2" fill="none"/></svg>Strata management work</li>
  <li><svg viewBox="0 0 10 10"><path d="M1 5l3 3 5-7" stroke="#f7901e" stroke-width="2" fill="none"/></svg>Pictures and white boards hung</li>
  <li><svg viewBox="0 0 10 10"><path d="M1 5l3 3 5-7" stroke="#f7901e" stroke-width="2" fill="none"/></svg>Windows and screens</li>
</ul>
<div class="abs btn-orange">▸ LEARN MORE</div>

<div class="abs page"></div>
<h2 class="abs feat-title"><svg viewBox="0 0 20 20"><path d="M10 1l2.6 6 6.4.5-4.9 4.2 1.5 6.3L10 14.6 4.4 18l1.5-6.3L1 7.5 7.4 7z" fill="#f7901e"/></svg>FEATURED PROJECTS</h2>
<div class="abs rule"></div>

<div class="abs card" style="left:147px"><div class="ph" role="img" aria-label="Family outside their home" style="background:linear-gradient(#9cc4d8,#7aa35a)"></div><h3>Home Owners</h3><p>Lorem Ipsum is simply dummy text of the printing and typesetting industry. Lorem Ipsum has been the industry's standard dummy text ever since the 1500s, when an unknown printer took a galley of type.</p><span class="arrow"><svg viewBox="0 0 21 21"><path d="M8 6l6 4.5L8 15z" fill="#fff"/></svg></span></div>
<div class="abs card" style="left:311px"><div class="ph" role="img" aria-label="Hard hat on building plans" style="background:linear-gradient(135deg,#c9d6e0,#e8b84a)"></div><h3>Project Tenders</h3><p>Lorem Ipsum is simply dummy text of the printing and typesetting industry. Lorem Ipsum has been the industry's standard dummy text ever since the 1500s, when an unknown printer took a galley of type.</p><span class="arrow"><svg viewBox="0 0 21 21"><path d="M8 6l6 4.5L8 15z" fill="#fff"/></svg></span></div>
<div class="abs card" style="left:473px"><div class="ph" role="img" aria-label="Office team joining hands" style="background:linear-gradient(#d8d2cc,#3a3a3a)"></div><h3>Office Managers</h3><p>Lorem Ipsum is simply dummy text of the printing and typesetting industry. Lorem Ipsum has been the industry's standard dummy text ever since the 1500s, when an unknown printer took a galley of type.</p><span class="arrow"><svg viewBox="0 0 21 21"><path d="M8 6l6 4.5L8 15z" fill="#fff"/></svg></span></div>
<div class="abs card" style="left:635px"><div class="ph" role="img" aria-label="Real estate agents in a meeting" style="background:linear-gradient(#c8ccd0,#4a4a4a)"></div><h3>Real Estate Agents</h3><p>Lorem Ipsum is simply dummy text of the printing and typesetting industry. Lorem Ipsum has been the industry's standard dummy text ever since the 1500s, when an unknown printer took a galley of type.</p><span class="arrow"><svg viewBox="0 0 21 21"><path d="M8 6l6 4.5L8 15z" fill="#fff"/></svg></span></div>

<section class="abs col" style="left:148px">
  <h4>Why We Are</h4>
  <div class="ph" role="img" aria-label="Business people shaking hands" style="background:linear-gradient(90deg,#e4e4e4,#3a3a3a)"></div>
  <p>Aenean elit commodo ligula lorem ante, dapibus in, viverra quis, feugiat a, tellus. Phasellus viverra nulla ut metus varius laoreet elementum semper nisi. Aenean vulputate eleifend tellus.</p>
  <div class="btn" style="width:62px;margin-top:8px;background:var(--orange)">Read More ›</div>
</section>
<section class="abs col" style="left:367px">
  <h4>How We Work</h4>
  <div class="ph" role="img" aria-label="Team hands stacked together" style="background:linear-gradient(135deg,#555,#c9a88a 50%,#333)"></div>
  <p>Aenean elit commodo ligula lorem ante, dapibus in, viverra quis, feugiat a, tellus. Phasellus viverra nulla ut metus varius laoreet elementum semper nisi. Aenean vulputate eleifend tellus.</p>
  <div class="btn" style="width:62px;margin-top:8px;background:var(--charcoal)">Read More ›</div>
</section>
<section class="abs col testi" style="left:582px">
  <h4>Testimonials</h4>
  <div class="quote-box">Aenean elit commodo ligula eget dolor. justo. Nullam dictum felis eu pede mollis pretium. Integer tincidunt. Cras dapibus. Vivamus elem entum semper nisi. Aenean vulputate eleifend tellus. Aenean leo ligula, vulputate eleifend tellus. porttitor consequat vitae, eleifend ac, enim.</div>
  <p class="author">Daniel Horne</p>
  <p class="role">Entrepreneur-in-Residence</p>
  <div class="btn view-all">View All ›</div>
</section>

<div class="abs partners-label">OUR PARTNERS</div>
<div class="abs partner" style="left:147px"><span></span><small>Click to See Future Plan</small></div>
<div class="abs partner" style="left:256px"><span></span><small style="color:var(--orange)">Click to See Future Plan</small></div>
<div class="abs partner" style="left:364px"><span></span><small>Click to See Future Plan</small></div>
<div class="abs partner" style="left:472px"><span></span><small>Click to See Future Plan</small></div>
<div class="abs partner" style="left:580px"><span></span><small>Click to See Future Plan</small></div>
<div class="abs partner" style="left:688px"><span></span><small>Click to See Future Plan</small></div>

<footer class="abs footer">
  <h5>TALL OAK RIDGE</h5>
  <nav>Home<i>•</i>About Us<i>•</i>Projects<i>•</i>Residential<i>•</i>Real Estate/Strata<i>•</i>Commercial<i>•</i>Quote<i>•</i>Blog<i>•</i>Contact Us<br>Terms of Use<i>•</i>Privacy Policy</nav>
  <div class="foot-badge">TALL OAK RIDGE<br>PROPERTY MAINTENANCE</div>
</footer>

<div class="abs bottom">
  <div class="label">Call Us</div>
  <div class="phone">0400 555 017</div>
  <div class="fine">All Right Reserved © 2012<br>Powered By : Brightline Studio</div>
</div>
</body>
</html>
```